Business cards Marta Kessel Sport & Events

I need new business cards to match my new logo design for my company called "Marta Kessel Sport & Events". I'm based in Germany.
With my company, I offer different services in the context of sport.

Marta Kessel owner

Marta Kessel Sports & Events
Birkenfelder Weg 12
D-63118 Offenbach

+49 69 / 31 52 94 07
info@marta-kessel.example
www.marta-kessel.example

Contact Information for Business Card

Marta Kessel Inhaberin Marta Kessel Sport & Events Birkenfelder Weg 12 D-63118 Offenbach +49 69 / 31 52 94 07 info@marta-kessel.example www.marta-kessel.example

Requirements
Must have
• Logo | Double sided business card

```html
<!DOCTYPE html>
<html lang="de">
<head>
<meta charset="utf-8">
<title>Marta Kessel Sport &amp; Events – Visitenkarte</title>
<link rel="stylesheet" href="https://fonts.googleapis.com/css2?family=Michroma&family=Arimo:wght@400;700&display=swap">
<style>
  :root {
    --orange: #f8a31d;
    --black: #101010;
    --white: #ffffff;
    --stage: #a3a3a3;
    --rule: #9a9a9a;
    --text: #141414;
  }
  * { margin: 0; padding: 0; box-sizing: border-box; }
  html, body { width: 1200px; height: 1200px; overflow: hidden; }
  body {
    background: var(--stage);
    position: relative;
    font-family: "Arimo", Arial, sans-serif;
    color: var(--text);
  }
  .card {
    position: absolute;
    top: 303px;
    width: 368px;
    height: 594px;
    overflow: hidden;
  }
  /* Front side */
  .card-front { left: 201px; background: var(--black); }
  .front-band-top {
    position: absolute; left: 0; top: 0;
    width: 113px; height: 343px;
    background: var(--orange);
  }
  .front-band-bottom {
    position: absolute; left: 0; top: 343px;
    width: 239px; height: 251px;
    background: var(--orange);
  }
  .front-name {
    position: absolute; left: 113px; right: 0; top: 190px;
    text-align: center;
    font-family: "Michroma", Arial, sans-serif;
    font-size: 22px;
    letter-spacing: 2px;
    color: var(--white);
    line-height: 1.4;
  }
  /* Back side */
  .card-back {
    left: 599px;
    background: var(--white);
    text-align: center;
  }
  .brand-dot {
    position: absolute; left: 50%; top: 73px;
    width: 108px; height: 108px; margin-left: -54px;
    border-radius: 50%;
    background: var(--orange);
  }
  .brand-name {
    position: absolute; left: 0; right: 0; top: 188px;
    font-family: "Michroma", Arial, sans-serif;
    font-size: 19px;
    letter-spacing: 1px;
    color: var(--black);
    line-height: 1.25;
  }
  .brand-name small {
    display: block;
    margin-top: 2px;
    font-size: 9px;
    letter-spacing: 6px;
  }
  .holder-name {
    position: absolute; left: 0; right: 0; top: 316px;
    font-family: "Michroma", Arial, sans-serif;
    font-size: 16px;
    letter-spacing: 2px;
    color: var(--black);
  }
  .holder-role {
    position: absolute; left: 0; right: 0; top: 340px;
    font-size: 16px;
    color: var(--orange);
  }
  .icon-row {
    position: absolute; left: 87px; top: 369px;
    width: 190px; height: 25px;
    display: flex; align-items: center; justify-content: center; gap: 4px;
  }
  .icon-row .rule { flex: 1; height: 1px; background: var(--rule); margin: 0 3px; }
  .icon {
    width: 25px; height: 25px;
    background: var(--orange);
    border-radius: 3px;
    display: flex; align-items: center; justify-content: center;
  }
  .contact {
    position: absolute; left: 0; right: 0; top: 408px;
    font-size: 16px; line-height: 21.5px;
  }
  .divider {
    position: absolute; left: 93px; top: 480px;
    width: 190px; height: 1px; background: var(--rule);
  }
  .address {
    position: absolute; left: 0; right: 0; top: 490px;
    font-size: 16px; line-height: 21.5px;
  }
  .address strong { color: var(--orange); font-weight: 700; }
</style>
</head>
<body>
  <section class="card card-front" aria-label="Vorderseite">
    <div class="front-band-top"></div>
    <div class="front-band-bottom"></div>
    <p class="front-name">MARTA<br>KESSEL</p>
  </section>

  <section class="card card-back" aria-label="Rückseite">
    <div class="brand-dot"></div>
    <p class="brand-name">MARTA KESSEL<small>SPORT &amp; EVENTS</small></p>

    <p class="holder-name">MARTA KESSEL</p>
    <p class="holder-role">Owner</p>

    <div class="icon-row">
      <span class="rule"></span>
      <span class="icon" aria-label="Telefon">
        <svg width="16" height="14" viewBox="0 0 16 14"><path d="M1 5c0-3 14-3 14 0v1h-3V4.5H4V6H1z" fill="#fff"/><path d="M4 7h8l2 6H2z" fill="#fff"/></svg>
      </span>
      <span class="icon" aria-label="E-Mail">
        <svg width="16" height="12" viewBox="0 0 16 12"><rect x="0.5" y="0.5" width="15" height="11" fill="none" stroke="#fff"/><path d="M0.5 0.5L8 7l7.5-6.5M0.5 11.5L6 6M15.5 11.5L10 6" fill="none" stroke="#fff"/></svg>
      </span>
      <span class="icon" aria-label="Web">
        <svg width="15" height="15" viewBox="0 0 15 15"><circle cx="7.5" cy="7.5" r="7" fill="#fff"/><path d="M4 4c2-1 3 1 2 3s1 3 0 5M10 3c-1 2 1 3 2 4" fill="none" stroke="#f8a31d" stroke-width="1.5"/></svg>
      </span>
      <span class="rule"></span>
    </div>

    <p class="contact">+49 69 / 31 52 94 07<br>info@marta-kessel.example<br>www.marta-kessel.example</p>
    <div class="divider"></div>
    <p class="address"><strong>Marta Kessel Sports &amp; Events</strong><br>Birkenfelder Weg 12<br>D-63118 Offenbach</p>
  </section>
</body>
</html>
```